Website Redesign - home improvements/garage door supplier & installer in London

We are a garage door specialist providing installation, automation and repair services throughout the South East England with 5 branches/showrooms across London and over 65 employees. Garage doors are our main area of expertise but we have other home improvement products in our range - front/entrance doors, internal doors, sliding and bi-fold patio doors; awnings and shading systems.

Our current website is quite boring and uninviting so we are looking to redesign and modernise the whole site to improve the user experience and flow.
Responsive, desktop and mobile friendly.

www.brightwellportals.example

Main pages to be templated:

Homepage
Category pages/list e.g. https://www.brightwellportals.example/garage-doors/
Basic content/product pages e.g https://www.brightwellportals.example/veltrop-internal-doors/
Main services pages e.g. https://www.brightwellportals.example/garage-door-installation/
Branch pages e.g. https://www.brightwellportals.example/branch-one/
Contact page
-----------------------
Our logo must stay as is (the attached AI file has 3 elements - logo -BRIGHTWELL PORTALS with the 'A'mark, the SINCE 1976 mark and a tagline 'Far beyond the everyday entrance' - these elements are to be used separately, not as a single block - although they can be combined)). Please use the text that’s already on the site in your design previews.
Our main colours are Blue RGB 35,57,119 and Red RGB 228,25,34

We would welcome a new smarter colour scheme but you will have to stick with the 2 primary colours we use on our logo - so any complimentary colours that might fit the new design would be great.

You can use all images that are on the website to support the new design - also attached is a zip with logo and images)

Target Market(s)

Most of our customers are in and around London - homeowners with garages that need servicing, replacing garage doors, upgrading or fitting new + other hiome improvements we can offer as listed above (fornt doors, bifold, sliding patio doors and awning) B2C

Industry/Entity Type

Home Improvement

Coding

Coded - Design and coding required

Font styles to use
Sans Serif

Requirements
Must have
• Custom and responsive design, user friendly, use our main 2 colours (red and blue described above) but add some complimentary colours to the mix
Nice to have
• Be creative, innovative
Should not have
• This should not be just some freely available wordpress template

```html
<!DOCTYPE html>
<html lang="en">
<head>
<meta charset="utf-8">
<title>Brightwell Portals – Home</title>
<link href="https://fonts.googleapis.com/css2?family=Arimo:wght@400;700&display=swap" rel="stylesheet">
<style>
:root{
  --blue:#2c308f;
  --brand-blue:#233977;
  --red:#e41922;
  --white:#ffffff;
  --field:#cfcfcf;
  --field-text:#6f6f6f;
  --gallery-bg:#cccccc;
  --ink:#1b1b1b;
  --shade:rgba(20,24,40,.55);
  --arrow:#3a3a3a;
  --copyright:#d9d9d9;
  --star:#f5c400;
}
*{box-sizing:border-box;margin:0;padding:0}
html,body{width:1200px;height:4532px;overflow:hidden}
body{position:relative;font-family:"Arimo",Arial,sans-serif;color:var(--ink);background:var(--white)}
.abs{position:absolute}

/* Header */
.site-header{left:0;top:0;width:1200px;height:192px;background:var(--white)}
.brand{left:28px;top:18px;width:370px;display:flex;align-items:center;gap:14px}
.brand-mark{flex:none;width:64px;height:64px;background:var(--red)}
.brand-name{font-weight:700;font-size:38px;line-height:40px;color:var(--brand-blue);letter-spacing:.5px}
.main-nav{left:420px;top:0;width:780px;height:112px;background:var(--blue);display:flex;align-items:center;justify-content:space-around;padding:0 20px}
.main-nav a{color:var(--white);text-decoration:none;font-weight:700;font-size:22px}

/* Hero */
.hero{left:0;top:192px;width:1200px;height:788px;overflow:hidden}
.hero-photo{position:absolute;inset:0;background:linear-gradient(180deg,#8fb2d6 0%,#c9d8e8 35%,#b89a86 55%,#d8d3cc 72%,#7f8a6e 100%)}
.hero-panel{left:272px;top:328px;width:656px;height:220px;background:var(--shade)}
.hero-title{left:272px;top:338px;width:656px;text-align:center;color:var(--white);font-weight:700;font-size:56px;line-height:96px}
.btn{display:flex;align-items:center;justify-content:center;text-align:center;color:var(--white);font-weight:700;text-decoration:none}
.btn-red{background:var(--red)}
.btn-blue{background:var(--blue)}
.hero-btn{left:456px;top:556px;width:324px;height:92px;font-size:24px;line-height:34px}
.slider-arrow{width:56px;height:72px;background:var(--arrow);display:flex;align-items:center;justify-content:center}
.hero .arrow-left{left:40px;top:408px}
.hero .arrow-right{left:1104px;top:408px}

/* About */
.about{left:0;top:992px;width:1200px;height:656px;overflow:hidden}
.about-photo{position:absolute;inset:0;background:linear-gradient(180deg,#9ec3e6 0%,#dfe8ef 40%,#f1f1ef 60%,#5c6a5a 100%)}
.about-panel{left:0;top:280px;width:1200px;height:376px;background:var(--shade)}
.about-title{left:0;top:294px;width:1200px;text-align:center;color:var(--white);font-weight:700;font-size:64px}
.about-text{left:112px;top:384px;width:976px;text-align:center;color:var(--white);font-size:23px;line-height:38px}
.about .btn{top:576px;height:56px;font-size:18px;font-weight:400;line-height:20px}
.about .btn-red{left:368px;width:204px}
.about .btn-blue{left:592px;width:208px}

/* Gallery */
.section-title{left:0;width:1200px;text-align:center;font-weight:700;font-size:48px}
.gallery-title{top:1694px}
.gallery-stage{left:40px;top:1760px;width:1120px;height:420px;background:var(--gallery-bg)}
.gallery-main{left:208px;top:0;width:712px;height:420px;background:linear-gradient(180deg,#e9ecee 0%,#cfd4d6 45%,#8d9497 70%,#c4c8c6 100%)}
.gallery-stage .arrow-left{left:152px;top:184px;width:48px;height:64px}
.gallery-stage .arrow-right{left:920px;top:184px;width:48px;height:64px}
.thumb{top:2200px;width:348px;height:232px}
.thumb-1{left:32px;background:linear-gradient(160deg,#dfe6ee 0%,#9aa7b4 55%,#5d5a55 100%)}
.thumb-2{left:420px;background:linear-gradient(180deg,#6fa0d8 0%,#a9c6e3 40%,#5c4630 70%,#3d5a2c 100%)}
.thumb-3{left:816px;background:linear-gradient(180deg,#7fb0e2 0%,#c9d9e8 35%,#7a4a2e 65%,#4a5a3a 100%)}

/* Testimonials */
.testimonials{left:0;top:2452px;width:1200px;height:508px;background:var(--blue);color:var(--white)}
.testimonials .section-title{top:44px;color:var(--ink)}
.quote{left:200px;top:132px;width:800px;text-align:center;font-weight:700;font-size:24px;line-height:36px}
.quote-source{left:0;top:236px;width:1200px;text-align:center;font-weight:700;font-size:15px}
.stars{left:460px;top:270px;display:flex;gap:18px}
.badges{left:364px;top:372px;display:flex;gap:28px;align-items:center}

/* Contact */
.contact-title{top:3112px}
.field{left:160px;width:828px;background:var(--field);color:var(--field-text);font-size:15px;padding:0 14px;display:flex;align-items:center}
.field-name{top:3204px;height:76px}
.field-address{top:3296px;height:76px}
.field-email{top:3412px;height:76px}
.field-message{top:3512px;height:280px;align-items:flex-start;padding-top:22px}
.send{left:720px;top:3828px;width:252px;height:72px;font-size:26px;font-weight:400}

/* Footer */
.site-footer{left:0;top:4012px;width:1200px;height:440px;background:var(--blue);color:var(--white);font-size:22px;line-height:32px}
.footer-col{top:56px}
.footer-col ul{list-style:none}
.col-office{left:72px}
.col-links{left:460px}
.col-guides{left:772px}
.copyright{left:0;top:4460px;width:1200px;height:72px;background:var(--copyright);text-align:center;font-size:22px;line-height:72px}
</style>
</head>
<body>

<header class="site-header abs">
  <div class="brand abs">
    <span class="brand-mark"></span>
    <span class="brand-name">BRIGHTWELL<br>PORTALS</span>
  </div>
  <nav class="main-nav abs">
    <a href="#">HOME</a>
    <a href="#">ABOUT US</a>
    <a href="#">GALLERY</a>
    <a href="#">TESTIMONIALS</a>
    <a href="#">CONTACT US</a>
  </nav>
</header>

<section class="hero abs">
  <div class="hero-photo" role="img" aria-label="House with a white sectional garage door under a blue sky"></div>
  <div class="hero-panel abs"></div>
  <h1 class="hero-title abs">FAR BEYOND THE<br>EVERYDAY ENTRANCE</h1>
  <a class="btn btn-red hero-btn abs" href="#">VIEW GUARAGE<br>DOOR TYPES</a>
  <div class="slider-arrow arrow-left abs"><svg width="22" height="34" viewBox="0 0 22 34"><path d="M18 3 4 17l14 14" fill="none" stroke="#fff" stroke-width="5"/></svg></div>
  <div class="slider-arrow arrow-right abs"><svg width="22" height="34" viewBox="0 0 22 34"><path d="M4 3l14 14L4 31" fill="none" stroke="#fff" stroke-width="5"/></svg></div>
</section>

<section class="about abs">
  <div class="about-photo" role="img" aria-label="Modern white house with a dark garage door"></div>
  <div class="about-panel abs"></div>
  <h2 class="about-title abs">ABOUT US</h2>
  <p class="about-text abs">Here at Brightwell Portals we’ve been putting our customers first for 40 years, providing thousands of garage doors throughout London and the South East. We work directly with leading manufacturers to bring you a premium garage door installation and repair facility.</p>
  <a class="btn btn-red abs" href="#">LEARN MORE</a>
  <a class="btn btn-blue abs" href="#">ALL OUR<br>SERVICES</a>
</section>

<h2 class="section-title gallery-title abs">GALLERY</h2>
<div class="gallery-stage abs">
  <div class="gallery-main abs" role="img" aria-label="Open bi-fold patio doors leading into a bright dining room"></div>
  <div class="slider-arrow arrow-left abs"><svg width="18" height="28" viewBox="0 0 18 28"><path d="M15 3 4 14l11 11" fill="none" stroke="#fff" stroke-width="4"/></svg></div>
  <div class="slider-arrow arrow-right abs"><svg width="18" height="28" viewBox="0 0 18 28"><path d="M3 3l11 11L3 25" fill="none" stroke="#fff" stroke-width="4"/></svg></div>
</div>
<div class="thumb thumb-1 abs" role="img" aria-label="Engineer fitting a garage door opener"></div>
<div class="thumb thumb-2 abs" role="img" aria-label="Double garage with timber doors"></div>
<div class="thumb thumb-3 abs" role="img" aria-label="Modern house with a wooden garage door"></div>

<section class="testimonials abs">
  <h2 class="section-title abs">TESTIMONIALS</h2>
  <p class="quote abs">"Initial visit within 24 hours of call. Work carried out within estimate of 2 weeks accepted. Work Manship was great"</p>
  <p class="quote-source abs">- Customer in Purley</p>
  <div class="stars abs">
    <svg width="38" height="38" viewBox="0 0 24 24"><path d="M12 1.5l3.1 6.6 7.2.9-5.3 5 1.4 7.1L12 17.6 5.6 21.1 7 14 1.7 9l7.2-.9z" fill="var(--star)"/></svg>
    <svg width="38" height="38" viewBox="0 0 24 24"><path d="M12 1.5l3.1 6.6 7.2.9-5.3 5 1.4 7.1L12 17.6 5.6 21.1 7 14 1.7 9l7.2-.9z" fill="var(--star)"/></svg>
    <svg width="38" height="38" viewBox="0 0 24 24"><path d="M12 1.5l3.1 6.6 7.2.9-5.3 5 1.4 7.1L12 17.6 5.6 21.1 7 14 1.7 9l7.2-.9z" fill="var(--star)"/></svg>
    <svg width="38" height="38" viewBox="0 0 24 24"><path d="M12 1.5l3.1 6.6 7.2.9-5.3 5 1.4 7.1L12 17.6 5.6 21.1 7 14 1.7 9l7.2-.9z" fill="var(--star)"/></svg>
    <svg width="38" height="38" viewBox="0 0 24 24"><path d="M12 1.5l3.1 6.6 7.2.9-5.3 5 1.4 7.1L12 17.6 5.6 21.1 7 14 1.7 9l7.2-.9z" fill="var(--star)"/></svg>
  </div>
  <div class="badges abs" aria-label="Trade accreditations">
    <svg width="112" height="104" viewBox="0 0 112 104"><rect x="0" y="0" width="112" height="104" rx="10" fill="#8a8a8a"/></svg>
    <svg width="128" height="104" viewBox="0 0 128 104"><rect x="0" y="0" width="128" height="104" fill="#6b6b6b"/></svg>
    <svg width="140" height="104" viewBox="0 0 140 104"><ellipse cx="70" cy="52" rx="70" ry="52" fill="#b9b9b9"/></svg>
  </div>
</section>

<h2 class="section-title contact-title abs">CONTACT US</h2>
<div class="field field-name abs">NAME</div>
<div class="field field-address abs">ADDRESS</div>
<div class="field field-email abs">EMAIL</div>
<div class="field field-message abs">MESSAGE</div>
<a class="btn btn-red send abs" href="#">SEND</a>

<footer class="site-footer abs">
  <div class="footer-col col-office abs">
    <p>Head Office Address:</p>
    <p>Brightwell Portals</p>
    <p>Meridian House, Larkspur Way</p>
    <p>Hollowbrook</p>
    <p>West Dunmore</p>
    <p>HB10 4QT</p>
    <p>&nbsp;</p>
    <p>Phone:</p>
    <p>0800 555 0142</p>
  </div>
  <div class="footer-col col-links abs">
    <ul>
      <li>Helpful links</li>
      <li>About Us</li>
      <li>Testimonials</li>
      <li>FAQs</li>
      <li>Request a Free Survey</li>
      <li>Terms &amp; Conditions</li>
      <li>Privacy Statement</li>
      <li>Careers</li>
    </ul>
  </div>
  <div class="footer-col col-guides abs">
    <ul>
      <li>Guides</li>
      <li>How to Order</li>
      <li>Choose The Door For You</li>
      <li>Download a Brochure</li>
      <li>Installation</li>
      <li>Garage Door Repairs</li>
      <li>Blog</li>
    </ul>
  </div>
</footer>
<div class="copyright abs">© 2018 All rights Reserved.</div>

</body>
</html>
```